BRIGHTWAVE DENTAL *

please see attached.

Target Market(s)

Adults 18-60

Contact Information for Business Card

Website: brightwavedentalqz.com
Phone number 555 304 7726 email: brightwavedentalqz@mailvex.com
Address:417 S. Kellim rd
Suite#24, TX70000
Dr. Elias Varno, DDS

Font styles to use
Sans Serif

Requirements
Must have
• Logo, phone number website, doctor,
• 's name

```html
<!DOCTYPE html>
<html lang="en">
<head>
<meta charset="utf-8">
<title>Brightwave Dental – Business Card</title>
<link rel="stylesheet" href="https://fonts.googleapis.com/css2?family=Jost:wght@300;400&family=Roboto:wght@300;400&display=swap">
<style>
  :root {
    --bg: #a9a6a7;
    --paper: #fbfbfa;
    --navy: #14263a;
    --teal: #1f7f98;
    --ink: #4a4747;
    --text: #3c3c3c;
  }
  * { box-sizing: border-box; margin: 0; padding: 0; }
  html, body { width: 1200px; height: 1200px; overflow: hidden; }
  body { background: var(--bg); position: relative; font-family: "Roboto", Arial, sans-serif; }

  .card {
    position: absolute;
    background: var(--paper);
    overflow: hidden;
  }
  .card--front { left: 238px; top: 118px; width: 712px; height: 420px; }
  .card--back  { left: 230px; top: 644px; width: 714px; height: 418px; }

  .brand-circle {
    position: absolute;
    border-radius: 50%;
    border: 2px solid var(--navy);
  }
  .card--front .brand-circle { left: 291px; top: 92px; width: 132px; height: 132px; }
  .card--back .brand-circle { left: 29px; top: 48px; width: 112px; height: 112px; border-color: var(--ink); }

  .brand-name {
    position: absolute;
    font-family: "Jost", Arial, sans-serif;
    font-weight: 400;
    white-space: nowrap;
  }
  .card--front .brand-name {
    left: 0; right: 0; top: 240px; text-align: center;
    font-size: 50px; color: var(--navy); letter-spacing: 1px;
  }
  .card--back .brand-name {
    left: 156px; top: 60px; font-size: 44px; color: var(--ink); letter-spacing: 1px;
  }

  .tagline {
    position: absolute;
    font-family: "Roboto", Arial, sans-serif;
    font-weight: 400;
    white-space: nowrap;
  }
  .card--front .tagline {
    left: 0; right: 0; top: 304px; text-align: center;
    font-size: 19px; letter-spacing: 2.6px; color: var(--navy);
  }
  .card--back .tagline {
    left: 157px; top: 120px; font-size: 19px; letter-spacing: 1.6px; color: var(--ink);
  }

  .doctor { position: absolute; left: 40px; top: 266px; }
  .doctor__name { font-size: 29px; color: var(--teal); font-weight: 400; margin-bottom: 6px; }
  .doctor__credential { font-size: 16.5px; color: var(--text); font-weight: 300; line-height: 21px; }

  .contact { position: absolute; left: 360px; top: 232px; font-size: 17.5px; color: var(--text); font-weight: 300; }
  .contact__row { display: flex; align-items: center; height: 26px; }
  .contact__icon { width: 18px; height: 14px; margin-right: 18px; fill: var(--teal); }
  .contact__address { margin-top: 8px; line-height: 27px; }

  .footer-band { position: absolute; left: 0; bottom: 0; width: 714px; height: 52px; }
  .website {
    position: absolute; left: 360px; bottom: 14px;
    font-size: 17.5px; color: #ffffff; font-weight: 300;
  }
</style>
</head>
<body>

  <section class="card card--front" aria-label="Card front">
    <div class="brand-circle"></div>
    <h1 class="brand-name">BRIGHTWAVE DENTAL</h1>
    <p class="tagline">GENERAL&nbsp; MODERN&nbsp; DENTISTRY</p>
  </section>

  <section class="card card--back" aria-label="Card back">
    <div class="brand-circle"></div>
    <h2 class="brand-name">BRIGHTWAVE DENTAL</h2>
    <p class="tagline">GENERAL MODERN DENTISTRY</p>

    <div class="doctor">
      <p class="doctor__name">Dr. Elias Varno</p>
      <p class="doctor__credential">Westmere College, BS, MCB</p>
      <p class="doctor__credential">Linden University, School of Dentistry, DDS</p>
      <p class="doctor__credential">US Army Veteran</p>
    </div>

    <div class="contact">
      <p class="contact__row">
        <svg class="contact__icon" viewBox="0 0 18 14" aria-hidden="true"><path d="M1 4 C4 0 14 0 17 4 L15 6 L12 5 L12 3 C10 2 8 2 6 3 L6 5 L3 6 Z M4 8 L14 8 L16 13 L2 13 Z"/></svg>
        555 304 7726
      </p>
      <p class="contact__row">
        <svg class="contact__icon" viewBox="0 0 18 14" aria-hidden="true"><path d="M1 1 H17 V13 H1 Z M2 2 L9 8 L16 2 Z" fill-rule="evenodd"/></svg>
        brightwavedentalqz@mailvex.com
      </p>
      <p class="contact__address">417 S. Kellim Rd. Suite#24.<br>Quarryton, TX 70000</p>
    </div>

    <svg class="footer-band" viewBox="0 0 714 52" aria-hidden="true">
      <rect x="0" y="36" width="300" height="16" fill="var(--teal)"/>
      <path d="M318 0 H714 V52 H292 Z" fill="var(--navy)"/>
    </svg>
    <p class="website">www.brightwavedentalqz.com</p>
  </section>

</body>
</html>
```